Beer Bottles and 6 Pack Case Design

Our Brewery's name is Quarry42 Brewing. We are looking for SEVEN bottle label designs. We are making this one project because we need all seven of the bottles labels to be different, but follow the same theme (as you will see in the attachments). The same goes for the six pack case design, same theme. As an added perk for the designers, we are willing to put "design by (you or your company)" on the bottle label designs and the six pack case. This will be seen by millions!!

The following are the names of our beers:
1) Plucked Wombat
2) KanTurnipo Jamma
3) Pearcastle Nectar
4) Runway Fringe IPA
5) Blue Cold Half-Aunt
6) Androids Called Otto
7) Copper Mule Limited

Our logo is also attached, please incorporate that into the designs (OR it can go on the neck of the bottle). If you have ANY questions, do not hesitate to ask!
Updates

Budgets for 2nd and 3rd place have been increased...

Project Deadline Extended
Reason: After posting this project I got very busy with other things and have not given this the attention I should have and have not responded to questions. Therefore I am going to extend the deadline by 7 days and answer all questions the best I can..

We have increased our first place budget to $500!!! 2nd and third place still get $100 each!!

Target Market(s)

The target market will be women and men, ages 24-34 with a slight focus towards the female demographic. Our target market annual income will be classified as middle to upper-middle class ($30,000- $60,000 annually).

Industry/Entity Type

It Company

Requirements
Nice to have
• Some sort of sketch of our "Characters" incorporated into the design.
Should not have
• -Many are submitting designs for the "androids called otto" label with pictures of t-rex dinosaurs. We would like just robots, no t-rex''s. Maybe a sketch of a few robots all with a "Hi My Name Is" sticker on them (like the stickers you get when you go to a big event. I have added an example of those stickers to the project attachments).
-We like the idea of a silly sketch of a donkey (possibly with a conductor hat and a whistle, but not a must) for the Copper Mule Limited label.
-We like the idea of a silly sketch of a shaven or partially shaven chinchilla for the Plucked Wombat label.
-We like the idea of a sketch of a women''s figure from behind with apples in place of her cheeks

Please take a look at the project attachment with the 9th Avenue beer bottle labels...we are leaning towards something along that sketch style design.

```html
<!DOCTYPE html>
<html lang="en">
<head>
<meta charset="utf-8">
<title>Pearcastle Nectar – Quarry42 Brewing</title>
<link rel="stylesheet" href="https://fonts.googleapis.com/css2?family=Roboto:wght@400;700&family=Rubik+Dirt&display=swap">
<style>
  :root {
    --page: #ffffff;
    --navy-center: #124386;
    --navy-edge: #0a2656;
    --line: #e9eef5;
    --ink: #ffffff;
    --title: #ececec;
    --honey: #f2b431;
    --apple: #c9322a;
  }
  html, body {
    margin: 0;
    width: 1200px;
    height: 1191px;
    overflow: hidden;
    background: var(--page);
  }
  .label {
    position: absolute;
    left: 83px;
    top: 154px;
    width: 1038px;
    height: 906px;
    background: radial-gradient(ellipse at 50% 45%, var(--navy-center) 0%, var(--navy-edge) 85%);
    font-family: "Roboto", Arial, sans-serif;
    color: var(--ink);
  }
  .frame {
    position: absolute;
    inset: 0;
  }
  .brand-name {
    position: absolute;
    left: 0;
    width: 100%;
    top: 150px;
    text-align: center;
    font-family: "Roboto", Arial, sans-serif;
    font-weight: 700;
    font-size: 52px;
    line-height: 1.1;
    letter-spacing: 4px;
    color: var(--ink);
    margin: 0;
  }
  .flavour-art {
    position: absolute;
    left: 367px;
    top: 399px;
    width: 291px;
    height: 243px;
    border-radius: 18px;
    background: radial-gradient(circle at 48% 45%, var(--apple) 0%, #d9642c 38%, var(--honey) 70%, rgba(242,180,49,0.85) 100%);
  }
  .beer-name {
    position: absolute;
    left: 0;
    width: 100%;
    top: 664px;
    margin: 0;
    text-align: center;
    font-family: "Rubik Dirt", Impact, sans-serif;
    font-weight: 400;
    font-size: 74px;
    line-height: 70px;
    color: var(--title);
    letter-spacing: 1px;
  }
  .side-text {
    position: absolute;
    text-align: center;
  }
  .legal {
    left: calc(107px - 330px);
    top: calc(453px - 36px);
    width: 660px;
    height: 72px;
    transform: rotate(90deg);
    font-size: 18px;
    line-height: 23px;
    text-transform: uppercase;
  }
  .story {
    left: calc(920px - 360px);
    top: calc(449px - 52px);
    width: 720px;
    height: 104px;
    transform: rotate(-90deg);
    font-size: 17.5px;
    line-height: 20.5px;
  }
  .story strong { font-weight: 400; }
</style>
</head>
<body>
  <main class="label">
    <svg class="frame" width="1038" height="906" viewBox="0 0 1038 906" aria-hidden="true">
      <g fill="none" stroke="var(--line)" stroke-width="2.5">
        <path d="M58 70 Q62 460 58 836"/>
        <path d="M981 70 Q977 460 981 836"/>
        <path d="M78 49 Q520 53 961 49"/>
        <path d="M78 856 Q520 852 961 856"/>
        <ellipse cx="62" cy="52" rx="16" ry="14"/>
        <ellipse cx="977" cy="52" rx="16" ry="14"/>
        <ellipse cx="62" cy="853" rx="16" ry="14"/>
        <ellipse cx="977" cy="853" rx="16" ry="14"/>
      </g>
    </svg>

    <h2 class="brand-name">QUARRY42<br>BREWING</h2>

    <div class="flavour-art" role="img" aria-label="Illustration of red and green apples, a sliced apple and cinnamon sticks on a honeycomb"></div>

    <h1 class="beer-name">PEARCASTLE<br>NECTAR</h1>

    <p class="side-text legal">
      CT IA NR MO TY -ME 12C+ 14C -OK+ FK<br>
      QUARRY42 BREWING CO., CITY, STATE - 12FL. OZ (355ML)<br>
      WWW.QUARRY42BREWING.COM
    </p>

    <p class="side-text story">
      <strong>Lorem Ipsum:</strong> is simply dummy text of the printing and typesetting industry.
      Lorem Ipsum has been the industry's standard dummy text ever since the
      1500s, when an unknown printer took a galley of type and scrambled it to
      make a type specimen book. It has survived not only five centuries, but also
      the leap into electronic typesetting, remaining essentially .
    </p>
  </main>
</body>
</html>
```